Plum Meadow Label

Design a label for new brand called Plum Meadow. The specific product label :
Plum Meadow Cocoa Butter Lotion. You only need to design the front label.
I have included the logo and a bottle jpeg with 2 bottles on it. Please try your best.

Industry/Entity Type

Product

Requirements
Must have
• text on the label other than the logo:
cocoa butter
lotion
8.5oz/250ml

Original Moisturizing Formula
Smoothes Marks
Protect Skin

__________________________________
- ALTERNATIVE TEXT TO ALSO USE:
Smoothes Dry Skin, Blemishes & Stretch Marks
Softens Hands, Face and Body
Vitamin E

```html
<!DOCTYPE html>
<html lang="en">
<head>
<meta charset="utf-8">
<title>Plum Meadow Cocoa Butter Lotion – Front Label</title>
<link href="https://fonts.googleapis.com/css2?family=Arimo:wght@400;700&family=Tinos:ital@1&display=swap" rel="stylesheet">
<style>
  :root {
    --page: #ffffff;
    --label-black: #1b1918;
    --brand-pink: #e3156f;
    --cocoa-cream: #e9dcc6;
    --text-white: #ffffff;
    --leaf-green: #4f6b3a;
    --leaf-light: #7f9a5c;
    --pod-brown: #5a3626;
    --pod-dark: #3a2218;
    --mint: #6b8d3a;
  }
  html, body {
    margin: 0;
    padding: 0;
    width: 1200px;
    height: 2166px;
    overflow: hidden;
    background: var(--page);
  }
  .canvas {
    position: relative;
    width: 1200px;
    height: 2166px;
    background: var(--page);
  }
  .front-label {
    position: absolute;
    left: 93px;
    top: 489px;
    width: 1014px;
    height: 1188px;
    background: var(--label-black);
    border-radius: 10px;
    overflow: hidden;
    font-family: "Arimo", Arial, sans-serif;
  }
  .art { position: absolute; z-index: 1; }
  .copy { position: absolute; z-index: 3; margin: 0; }
  .brand-name {
    left: 0;
    top: 118px;
    width: 1014px;
    text-align: center;
    font-family: "Arimo", Arial, sans-serif;
    font-weight: 700;
    font-size: 104px;
    line-height: 1;
    color: var(--brand-pink);
  }
  .product-name {
    left: 0;
    top: 290px;
    width: 1014px;
    text-align: center;
    font-weight: 400;
    font-size: 78px;
    line-height: 1;
    color: var(--cocoa-cream);
  }
  .leaf-art {
    left: 735px;
    top: 290px;
    width: 230px;
    height: 320px;
    border-radius: 50% 50% 50% 50% / 60% 60% 40% 40%;
    background: radial-gradient(ellipse at 45% 40%, var(--leaf-light), var(--leaf-green));
  }
  .type-band {
    position: absolute;
    z-index: 2;
    left: 0;
    top: 453px;
    width: 1014px;
    height: 184px;
    background: var(--brand-pink);
  }
  .type-band__text {
    position: absolute;
    left: 34px;
    top: 26px;
    margin: 0;
    font-weight: 400;
    font-size: 70px;
    line-height: 1.07;
    color: var(--text-white);
    letter-spacing: 1px;
  }
  .pod-art {
    z-index: 2;
    left: 620px;
    top: 556px;
    width: 245px;
    height: 178px;
    border-radius: 50%;
    background: radial-gradient(ellipse at 40% 35%, #7a4a34, var(--pod-brown) 55%, var(--pod-dark));
  }
  .vitamin-note {
    left: 34px;
    top: 698px;
    font-family: "Tinos", Georgia, serif;
    font-style: italic;
    font-size: 38px;
    line-height: 1;
    color: var(--text-white);
  }
  .benefits {
    right: 130px;
    top: 770px;
    padding: 0;
    list-style: none;
    text-align: right;
    font-size: 40px;
    line-height: 49px;
    color: var(--text-white);
  }
  .mint-sprig {
    border-radius: 50% 10% 50% 10%;
    background: radial-gradient(ellipse at 50% 50%, #8fae52, var(--mint));
  }
  .mint-sprig--right { left: 896px; top: 748px; width: 74px; height: 78px; }
  .mint-sprig--left  { left: 140px; top: 944px; width: 134px; height: 122px; }
  .net-content {
    left: 0;
    top: 1010px;
    width: 1014px;
    text-align: center;
    font-size: 36px;
    color: var(--text-white);
  }
</style>
</head>
<body>
<main class="canvas">
  <section class="front-label" aria-label="Plum Meadow Cocoa Butter Lotion front label">
    <div class="art leaf-art" role="img" aria-label="Illustration of a green cocoa leaf"></div>
    <h1 class="copy brand-name">Plum Meadow</h1>
    <h2 class="copy product-name">Cocoa Butter</h2>
    <div class="type-band">
      <p class="type-band__text">HAND &amp; BODY<br>LOTION</p>
    </div>
    <div class="art pod-art" role="img" aria-label="Illustration of a brown cocoa pod"></div>
    <p class="copy vitamin-note">with Vitamin E</p>
    <div class="art mint-sprig mint-sprig--right" role="img" aria-label="Small mint leaf decoration"></div>
    <ul class="copy benefits">
      <li>Original</li>
      <li>Moisturizing Formula</li>
      <li>Smoothes Marks</li>
      <li>Protects Skin</li>
    </ul>
    <div class="art mint-sprig mint-sprig--left" role="img" aria-label="Small mint leaf decoration"></div>
    <p class="copy net-content">8.5oz/250ml</p>
  </section>
</main>
</body>
</html>
```